6' Banner Stands for exhibiting to Health Fairs with an audience of age 55+

We need designs for two 6' banner stands to stand on either side of our exhibition tables. We offer Hereditary Cancer Screening. I want the banners to have the same look and feel as the logo and the files color scheme logo, etc..

The Banners should have "Hereditary Cancer Screening" at the top with the Tag Line "The Test You Take For Them" underneath. A photo of grandparents with kids/grandkids and underneath the photos in large font one of the following messages:
1) "A Simple Swab Could Save A Family Members LIFE Get Tested Today!"
2) "Does Cancer Run In Your Family? Get Tested Today!"
3) "Knowledge Is Power" "Get Tested Today!"
4) "Will You Give Your Loved Ones The Information To Beat Cancer In Their Lives? Get Tested Today!
5) Knowledge Is Power Get Tested Today!"
Updates

Thank you all for your designs I now have the exact specs for the banners, so please use these as you update your designs. 31.5 inches X 83.25 inches and add a 1/2 inch bleed to all 4 sides. Thank you.

Target Market(s)

Persons 55+ who are grandparents

Industry/Entity Type

Healthcare

Font styles to use
Sans Serif
Other font styles liked:
• Comic Sans for "The Test You Take For Them"

Colors
9bcb3c
0356a4
ffffff

Requirements
Must have
• the main focus should be the hereditary cancer screening; "Hereditary Cancer Screening";
• "The test you order for them" in Comic Sans font underneath
• A photo or photos of grandparents with their grandchildren (multiple ethnicities)
• One of the slogans listed above
• GET TESTED TODAY underneath the messages at the bottom of the banner highlighted and eye catching
• www.kinhealthcheckup.net
Nice to have
• Logo at the top or bottom

```html
<!DOCTYPE html>
<html lang="en">
<head>
<meta charset="utf-8">
<title>Hereditary Cancer Screening – Banner Stand</title>
<link rel="stylesheet" href="https://fonts.googleapis.com/css2?family=Comic+Neue:wght@700&family=Libre+Baskerville:wght@700&family=Raleway:wght@500;700;800;900&display=swap">
<style>
  :root {
    --navy: #14225a;
    --green: #8cc63f;
    --white: #ffffff;
    --photo-warm: #d8b59a;
    --photo-soft: #c9a78c;
  }
  * { margin: 0; padding: 0; box-sizing: border-box; }
  html, body { width: 1200px; height: 3113px; overflow: hidden; background: var(--white); }
  .banner {
    position: relative;
    width: 1200px;
    height: 3113px;
    background: var(--white);
    font-family: "Raleway", Arial, sans-serif;
    color: var(--navy);
  }
  .tagline-band {
    height: 150px;
    background: var(--navy);
    display: flex;
    align-items: center;
    justify-content: center;
  }
  .tagline {
    font-family: "Comic Neue", "Comic Sans MS", cursive;
    font-weight: 700;
    font-size: 68px;
    letter-spacing: 2px;
    color: var(--green);
  }
  .headline {
    margin-top: 48px;
    text-align: center;
    font-family: "Libre Baskerville", Georgia, serif;
    font-weight: 700;
    font-size: 146px;
    line-height: 170px;
    color: var(--navy);
  }
  .photo-grid {
    position: absolute;
    top: 818px;
    left: 0;
    width: 1200px;
    height: 690px;
    background: var(--green);
    padding: 10px 0;
    display: grid;
    grid-template-columns: repeat(3, 1fr);
    grid-template-rows: repeat(2, 1fr);
    gap: 8px;
  }
  .photo { background: linear-gradient(135deg, var(--photo-warm), var(--photo-soft)); }
  .photo:nth-child(2) { background: linear-gradient(135deg, #c99a7c, #a8806a); }
  .photo:nth-child(3) { background: linear-gradient(135deg, #b58a6e, #8f6a58); }
  .photo:nth-child(4) { background: linear-gradient(135deg, #d6b89c, #9c7560); }
  .photo:nth-child(5) { background: linear-gradient(135deg, #a9b894, #c0a894); }
  .photo:nth-child(6) { background: linear-gradient(135deg, #c7a68e, #a47a66); }
  .message {
    position: absolute;
    top: 1570px;
    left: 0;
    width: 1200px;
    text-align: center;
  }
  .message-line {
    font-size: 80px;
    font-weight: 500;
    line-height: 110px;
  }
  .message-line strong { font-weight: 700; }
  .message-key {
    font-weight: 900;
    font-size: 318px;
    line-height: 320px;
    letter-spacing: -4px;
    color: var(--green);
    text-shadow: 9px 9px 0 var(--navy);
  }
  .message-key.save { margin: 10px 0 20px; }
  .message-key.life { margin-top: 12px; }
  .cta-band {
    position: absolute;
    top: 2469px;
    left: 0;
    width: 1200px;
    height: 184px;
    background: var(--navy);
    display: flex;
    align-items: center;
    justify-content: center;
  }
  .cta {
    font-weight: 800;
    font-size: 116px;
    color: var(--green);
  }
  .brand {
    position: absolute;
    top: 2710px;
    left: 0;
    width: 1200px;
    display: flex;
    align-items: center;
    justify-content: center;
    gap: 36px;
  }
  .brand-mark {
    width: 170px;
    height: 170px;
    border-radius: 50%;
    background: var(--navy);
  }
  .brand-name {
    font-family: "Raleway", Arial, sans-serif;
    font-weight: 800;
    font-size: 70px;
    line-height: 62px;
    color: var(--navy);
    text-transform: uppercase;
  }
  .website {
    position: absolute;
    top: 2960px;
    left: 0;
    width: 1200px;
    text-align: center;
    font-weight: 500;
    font-size: 56px;
    color: var(--navy);
  }
</style>
</head>
<body>
<main class="banner">
  <header class="tagline-band">
    <p class="tagline">“The Test You Take For Them”</p>
  </header>
  <h1 class="headline">Hereditary<br>Cancer<br>Screening</h1>

  <section class="photo-grid">
    <div class="photo" role="img" aria-label="Grandmother hugging a young granddaughter"></div>
    <div class="photo" role="img" aria-label="Grandfather receiving a kiss from his grandchild"></div>
    <div class="photo" role="img" aria-label="Grandmother embracing her granddaughter"></div>
    <div class="photo" role="img" aria-label="Grandfather cheek to cheek with his granddaughter"></div>
    <div class="photo" role="img" aria-label="Grandfather holding his young grandson outdoors"></div>
    <div class="photo" role="img" aria-label="Smiling grandmother with granddaughter hugging her shoulders"></div>
  </section>

  <section class="message">
    <p class="message-line">A Simple Swab <strong>Could</strong></p>
    <p class="message-key save">SAVE</p>
    <p class="message-line">a Family Members</p>
    <p class="message-key life">LIFE</p>
  </section>

  <div class="cta-band">
    <p class="cta">Get Tested Today!</p>
  </div>

  <footer>
    <div class="brand">
      <span class="brand-mark" aria-hidden="true"></span>
      <p class="brand-name">Kinward<br>Health<br>Group</p>
    </div>
    <p class="website">www.kinhealthcheckup.net</p>
  </footer>
</main>
</body>
</html>
```